Larkspur Ridge Management - Business Cards

I need business cards. My current logo was designed by a designer at this site and I very much like and am happy with the results. I would like a business card that is trendy, unique, current yet professional. I deal with high net worth clients daily

Target Market(s)

Out of state investors looking to get into the rental market in Ohio

Industry/Entity Type

Property Management, Consulting

Contact Information for Business Card

Name, Title (Chief Financial Officer) office phone number (555) 817-3094 website address larkridgemgmt.example

Font styles to use
Sans Serif

Colors
0054AA
0677BA
7BADD7
CADEEF
E8F1F8
0094D4
00A9DD
6FCCEA
C7EBF8
E9F6FB
00AB8E
00BBA5
67D7C9
C6EFE9
E9F9F6

```html
<!DOCTYPE html>
<html lang="en">
<head>
<meta charset="utf-8">
<title>Larkspur Ridge Management – Business Cards</title>
<link rel="stylesheet" href="https://fonts.googleapis.com/css2?family=Figtree:wght@400;600;800&display=swap">
<style>
  :root {
    --navy: #21325a;
    --red: #d0272f;
    --white: #ffffff;
    --backdrop: #ececec;
  }
  html, body {
    margin: 0;
    padding: 0;
    width: 1200px;
    height: 1200px;
    overflow: hidden;
    background: var(--backdrop);
    font-family: "Figtree", sans-serif;
  }
  .card-set {
    position: relative;
    width: 1200px;
    height: 1200px;
  }
  .card {
    position: absolute;
    top: 169px;
    width: 494px;
    height: 862px;
    background: var(--white);
  }
  .card--front { left: 90px; }
  .card--back { left: 617px; }
  .card svg { display: block; width: 100%; height: 100%; }
  .wordmark {
    font-family: "Figtree", sans-serif;
    font-weight: 800;
    fill: var(--navy);
  }
  .holder-name { font-family: "Figtree", sans-serif; font-weight: 600; fill: var(--white); }
  .holder-title,
  .contact-line { font-family: "Figtree", sans-serif; font-weight: 400; fill: var(--white); }
</style>
</head>
<body>
<main class="card-set">

  <section class="card card--front" aria-label="Business card front">
    <svg viewBox="0 0 395 690" xmlns="http://www.w3.org/2000/svg">
      <g class="brand-block">
        <text class="wordmark" x="197.5" y="150" font-size="30" text-anchor="middle">Larkspur Ridge</text>
        <text class="wordmark" x="197.5" y="186" font-size="30" text-anchor="middle">Management</text>
      </g>

      <path class="house-panel" d="M0,455 L198,330 L395,455 V690 H0 Z" fill="var(--navy)"/>
      <path class="house-frame" d="M25,465 L198,359 L371,465 V665 H25 Z" fill="none" stroke="var(--white)" stroke-width="2"/>
      <path class="roof-accent" d="M118,410 L198,357 L278,410 Z" fill="var(--red)"/>

      <text class="holder-name" x="198" y="492" font-size="27" text-anchor="middle">Your Name</text>
      <text class="holder-title" x="198" y="522" font-size="17" text-anchor="middle">Chief Financial Officer</text>

      <g class="contact-phone">
        <path d="M111,579 c1,-1 3,-1 4,0 l2,2 c1,1 1,2 0,3 l-1,1 c1,2 3,4 5,5 l1,-1 c1,-1 2,-1 3,0 l2,2 c1,1 1,3 0,4 l-1,1 c-6,1 -16,-9 -15,-15 Z" fill="var(--white)"/>
        <text class="contact-line" x="134" y="591" font-size="17">(555) 817-3094</text>
      </g>
      <g class="contact-web">
        <circle cx="117" cy="613" r="6.5" fill="none" stroke="var(--white)" stroke-width="1.6"/>
        <ellipse cx="117" cy="613" rx="2.6" ry="6.5" fill="none" stroke="var(--white)" stroke-width="1.2"/>
        <line x1="110.5" y1="613" x2="123.5" y2="613" stroke="var(--white)" stroke-width="1.2"/>
        <text class="contact-line" x="134" y="619" font-size="17">larkridgemgmt.example</text>
      </g>
    </svg>
  </section>

  <section class="card card--back" aria-label="Business card back">
    <svg viewBox="0 0 395 690" xmlns="http://www.w3.org/2000/svg">
      <g class="brand-block">
        <text class="wordmark" x="197.5" y="330" font-size="34" text-anchor="middle">Larkspur Ridge</text>
        <text class="wordmark" x="197.5" y="372" font-size="34" text-anchor="middle">Management</text>
      </g>
    </svg>
  </section>

</main>
</body>
</html>
```